Flyer for promoting a hotel in the beach in miami for an event

We are are Coral Tern Stays and have a resort at Miami, Hallandale Beach.
We need a triptych:
- With a lot of photos to show the clients the wonderful experience they can live with their families going on vacations to miami.
- We want the amenities and photos of the units to stand out.
I attached a document called Triptico that is a guide for you to know what we want, and another called . When you do your design you must know that:
- The text should be linked to each photo. All the photos are attached.
- There is freedom to play with the structure. I did an example, but PLEASE mix this up and do it less structured.
- You can feel free to add any other photos at the background, from the ones I sent or from other places. Like for example of a family.

Target Market(s)

Families who go to vacaton to have a great experience and memories. Targeted to people who love the beach and miami

Industry/Entity Type

Hotel

Font styles to use
Sans Serif

Colors
ec1f27
ffffff

Requirements
Must have
• The photos with numbers

```html
<!DOCTYPE html>
<html lang="en">
<head>
<meta charset="utf-8">
<title>Coral Tern Stays – Trifold Brochure</title>
<link rel="stylesheet" href="https://fonts.googleapis.com/css2?family=Cinzel:wght@400;700&family=Roboto+Condensed:wght@400;700&family=Open+Sans:wght@400;700&display=swap">
<style>
  :root {
    --brand-red: #ec1f27;
    --deep-red: #a5141a;
    --white: #ffffff;
    --stage: #dcdcdc;
    --ink: #2b2b2b;
    --band-grey: rgba(150, 150, 150, 0.88);
  }
  * { box-sizing: border-box; margin: 0; padding: 0; }
  html, body { width: 754px; height: 1200px; overflow: hidden; }
  body {
    background: var(--stage);
    font-family: "Open Sans", Arial, sans-serif;
    color: var(--ink);
  }
  .brochure {
    position: absolute;
    left: 17px; top: 322px;
    width: 720px; height: 556px;
    display: flex;
    box-shadow: 0 8px 22px rgba(0,0,0,0.28);
  }
  .panel { position: relative; width: 240px; height: 100%; overflow: hidden; }
  .photo { position: absolute; }
  .photo-number {
    position: absolute;
    width: 18px; height: 18px; border-radius: 50%;
    background: var(--brand-red); color: var(--white);
    border: 1.5px solid var(--white);
    font-family: "Roboto Condensed", Arial, sans-serif; font-weight: 700; font-size: 10px;
    line-height: 15px; text-align: center;
  }

  /* Left panel */
  .panel--story { background: #3f7f98; }
  .story-backdrop {
    inset: 0;
    background: linear-gradient(180deg, #3aa6cf 0%, #8cc8e2 28%, #5d8fa8 58%, #2f5d70 100%);
  }
  .story-backdrop .photo-number { left: 6px; top: 6px; }
  .story-card {
    position: absolute; left: 24px; top: 30px; width: 199px; height: 476px;
    background: rgba(255,255,255,0.78);
    text-align: center;
    padding: 0 10px;
  }
  .story-photo {
    position: relative;
    display: block; margin: 16px auto 0;
    width: 120px; height: 120px; border-radius: 50%;
    border: 3px solid var(--brand-red);
    background: linear-gradient(180deg, #5e9fd8 0%, #b9d6ee 45%, #c9b79a 70%, #6b5a48 100%);
  }
  .story-photo .photo-number { right: -4px; top: 4px; }
  .story-title {
    font-family: "Roboto Condensed", Arial, sans-serif;
    font-weight: 700; font-size: 12.5px;
    color: var(--brand-red);
    margin: 10px 0 12px;
  }
  .story-text { font-size: 8.3px; line-height: 1.38; color: #333; margin-bottom: 11px; }
  .story-text b { font-weight: 700; }
  .panel-footer {
    position: absolute; left: 0; bottom: 0; width: 100%; height: 36px;
    display: flex; align-items: center; justify-content: center;
    font-family: "Cinzel", Georgia, serif; font-size: 10px; letter-spacing: 0.3px;
  }
  .panel--story .panel-footer { background: var(--band-grey); color: #222; }

  /* Middle panel */
  .panel--contact {
    background: radial-gradient(ellipse at 50% 45%, var(--brand-red) 0%, #c8161d 55%, var(--deep-red) 100%);
    color: var(--white); text-align: center;
  }
  .map-spot {
    position: absolute; left: 59px; top: 40px;
    width: 122px; height: 122px; border-radius: 50%;
    border: 3px solid var(--white);
    background: radial-gradient(circle at 50% 45%, #eeeae2 0%, #dfe3e8 60%, #b9cde6 100%);
  }
  .contact-title {
    position: absolute; left: 0; top: 256px; width: 100%;
    font-family: "Roboto Condensed", Arial, sans-serif; font-weight: 700; font-size: 11.5px;
  }
  .contact-list { position: absolute; left: 0; top: 280px; width: 100%; list-style: none; }
  .contact-list li {
    font-family: "Roboto Condensed", Arial, sans-serif; font-size: 8.6px; line-height: 1.3;
    margin-bottom: 9px;
  }
  .contact-list svg { display: block; margin: 0 auto 3px; width: 11px; height: 11px; }
  .panel--contact .panel-footer { color: var(--white); }

  /* Right panel */
  .panel--cover { background: #5f8fbf; }
  .cover-photo {
    inset: 0;
    background: linear-gradient(180deg, #2f6fc4 0%, #6fa0d8 30%, #c9d2dc 58%, #e6e8ea 70%, #7aa06c 84%, #4f7f90 100%);
  }
  .cover-photo .photo-number { right: 6px; top: 6px; }
  .cover-band {
    position: absolute; left: 0; top: 178px; width: 100%; height: 168px;
    background: rgba(120,130,140,0.72);
    text-align: center; color: var(--white);
  }
  .cover-welcome {
    font-family: "Cinzel", Georgia, serif; font-weight: 700; font-size: 28px; line-height: 1.05;
    margin-top: 16px; letter-spacing: 1px;
  }
  .cover-brand {
    font-family: "Roboto Condensed", Arial, sans-serif; font-weight: 700; font-size: 22px;
    color: var(--brand-red); margin-top: 6px; letter-spacing: 0.5px;
  }
  .cover-tagline {
    font-family: "Cinzel", Georgia, serif; font-size: 9px; line-height: 1.35; margin-top: 10px;
  }
  .panel--cover .panel-footer { height: 24px; background: rgba(210,210,210,0.92); color: #222; }
</style>
</head>
<body>
  <main class="brochure">
    <section class="panel panel--story">
      <div class="photo story-backdrop" role="img" aria-label="Photo 1: aerial view of the Miami shoreline and city towers">
        <span class="photo-number">1</span>
      </div>
      <div class="story-card">
        <div class="story-photo" role="img" aria-label="Photo 2: exterior of the new apartment building">
          <span class="photo-number">2</span>
        </div>
        <h2 class="story-title">BRAND NEW APARTMENTS!</h2>
        <p class="story-text">The resort combines a great location, high-style and casual vibes specially to take advantage of shopping, beautiful weather, sandy beaches, racetracks, gaming and more.</p>
        <p class="story-text">This <b>luxurious resort</b> is a perfect place for people looking for a peaceful atmosphere and high standards to <b>enjoy their vacations with family and friends</b>. The interiors are designed by Velanti Studio, independent Italian Corsa designer, and all furnishers are contemporary Italian design. Several types of apartments are available:</p>
        <p class="story-text">Studio Suite, One Bedroom, Two Bedroom or Three Bedroom, we make sure to offer you the best installation for your <b>stay in Miami</b>. Coral Tern Stays' guests can enjoy all the services and amenities of the resort.</p>
      </div>
      <footer class="panel-footer">WWW.CORALTERNSTAYS.CLUB</footer>
    </section>

    <section class="panel panel--contact">
      <div class="map-spot" role="img" aria-label="Map showing the resort location"></div>
      <h2 class="contact-title">FEEL FREE TO CALL US ANY TIME</h2>
      <ul class="contact-list">
        <li>
          <svg viewBox="0 0 12 12" fill="none" stroke="#fff" stroke-width="1"><circle cx="6" cy="6" r="5"/><ellipse cx="6" cy="6" rx="2.2" ry="5"/><path d="M1 6h10M2 3.3h8M2 8.7h8"/></svg>
          WWW.CORALTERNSTAYS.CLUB
        </li>
        <li>
          <svg viewBox="0 0 12 12" fill="#fff"><path d="M0 2h12v8H0z"/><path d="M0.5 2.5 6 7l5.5-4.5" fill="none" stroke="#c8161d" stroke-width="1"/></svg>
          INQUIRY@CORALTERNSTAYS.COM
        </li>
        <li>
          <svg viewBox="0 0 12 12" fill="none" stroke="#fff" stroke-width="1"><circle cx="6" cy="6" r="5.2"/><path d="M4 3.2c-.6.4-.6 1.6.6 3.1s2.3 2.1 2.9 1.6l.5-.6-1.1-.9-.6.4c-.5-.2-1.2-1-1.4-1.5l.4-.6-.8-1.1z" fill="#fff" stroke="none"/></svg>
          USA: +1-(555)-014-2200<br>CL: +56 (2) 2000-0147
        </li>
        <li>
          <svg viewBox="0 0 12 12" fill="#fff"><path d="M6 0.5a3.6 3.6 0 0 0-3.6 3.6C2.4 7 6 11.5 6 11.5s3.6-4.5 3.6-7.4A3.6 3.6 0 0 0 6 .5z"/><circle cx="6" cy="4.1" r="1.3" fill="#c8161d"/></svg>
          HOLLYWOOD/HALLANDALE:<br>1480 SEAGRAPE SHORE DRIVE
        </li>
      </ul>
      <footer class="panel-footer">WWW.CORALTERNSTAYS.CLUB</footer>
    </section>

    <section class="panel panel--cover">
      <div class="photo cover-photo" role="img" aria-label="Photo 3: white beachfront resort tower with pool and palms by the water">
        <span class="photo-number">3</span>
      </div>
      <div class="cover-band">
        <h1 class="cover-welcome">WELCOME<br>TO</h1>
        <div class="cover-brand">CORAL TERN STAYS</div>
        <p class="cover-tagline">LUXURY RESORT CONDOMINIUMS &amp;<br>EXCLUSIVE BEACH CLUB</p>
      </div>
      <footer class="panel-footer">WWW.CORALTERNSTAYS.CLUB</footer>
    </section>
  </main>
</body>
</html>
```